Relaunch of company website (Technical company)

Hi all,

we need a website based on Wordpress who makes the customer curious and excited of all the possibilities we can offer.
Customers are B2B. The layout should be based on the screenshots I added, but refreshed and modernized with some nice gadgets.
All needs to be responsive for the different devices.
We are a technical company. We provide a full range of service from 3D scan, Manufacturing, Prototyping, Bulk production and CAD service.

Later the website needs to have a multi language option.

Home:

1. Logo top left (attached)
2. Menu bar top right
3. Header picture like in the screenshot
4. Than the three small blue pics (CAD - Fertigung - Manufaktur) we want a
hoover-small zoom effect as soon as the mouse hits them.
5. Introduction text of our company
6. Contact Information (Design sample see attachment)
7. At the end "Impressum - Datenschutzerklärung - Haftungsausschluss. Those need to be linked to extra pages where we can add mandatory text (Legal notice, Privacy, Disclaimer)

Leistungen - Our service:

1. See the attachment named our service.
2. First on page a gallery where we can add pictures. If moving the mouse over the picture we want a one line explanation e.g. 3D Scan, Production, Die cast...
no click option at the pictures, just to see.
3. Below that, a side menu (we need to add or remove items by our self if necessary) on the left where we can add our service.
4. If the customer is clicking a service, it needs to be highlighted
5. After clicking a service we want our text to that service appear right of the menu (see attachment sample) and 2 big pictures on top of the menu and text field.

Gallery:

1. Headline pictures for each gallery Category (6-8 at the moment)
2. Mouse over the picture zooms it a little in and adds a text what category it is
e.g. Reverse engineering, Prototyping, Laserscan
3. Clicking on the picture opens the detail gallery to that category. There we need
to add pictures specific to that service.
4. If the customer is clicking on a picture from there, all pictures from that
Category will open in a full screen view mode

Blog:

1. A blog to add news (picture and text). Right now we don´t have the time to feed
it, so we want to deactivate it as long as we cant keep it up to date. Later it
should be part of the website.

Unternehmen:

1. Drop down menu: Our Team - History - Unsere Partner - AGB - Impressum

Our Team:
1. Short description of our employees including picture (see attachment)
2. Contact Information (Design sample see attachment)
3. At the end "Impressum - Datenschutzerklärung - Haftungsausschluss. Those need to be linked to extra pages where we can add mandatory text (Legal notice, Privacy, Disclaimer)

History:
1. Timeline where we can add milestones including date, and pictures of the company (see screenshot)

Unsere Partner:
1. Text field where we can introduce our partners including pictures if necessary.

A blog would be a nice option, social media shortcuts to Instagram-FB but no preview of FB Timeline within the website.

We do have professional text already, that will be added by us. We expect you to use any sample text and pictures for the draft, beside what we supply already.

If you see the need of buying pictures from Quorvane or any other picture company that is OK for us.

What we expect:

A modern, fresh website based on our existing design, changes are fine as long as the whole website design does not change completely to an unicorn thing in pink. Feel free to be creative. New ideas will be discussed, we are open to good ideas. We don´t stick fix to our idea, but we want our customers can see that its still the same company.
Scrolling effects would be a nice gadget if possible.

We have a bad page already...don´t want a second bad one :-)

Our company blue is RBG 106, 206, 224

Greets to all, looking for professional results.

Target Market(s)

B2B, Engineering companys,

Industry/Entity Type

Technical Service

Number of Pages Required

5+ page

Font styles to use
Sans Serif
Other font styles liked:
• verdana

Colors
0455a3
000000
ffffff

Requirements
Must have
• Responsive design, We want to be able to add posts to the Blog, pictures to the categories, and categories by ourself if necessary. (Wordpress)
• Lets say we want to add one more category at „Leistungen-Our Service“ that should be possible for us in the wordpress background.
Nice to have
• Dynamic elements to make the website more alive.
Should not have
• Sliders, Contact form

```html
<!DOCTYPE html>
<html lang="de">
<head>
<meta charset="utf-8">
<title>Norvik Precision – Galerie</title>
<link rel="stylesheet" href="https://fonts.googleapis.com/css2?family=Montserrat:wght@400;500;600;700&family=Lato:wght@700;900&display=swap">
<style>
  :root {
    --brand-blue: #0455a3;
    --button-blue: #1a63b0;
    --tile-light: #5ab1cd;
    --tile-dark: #0c4d91;
    --tile-mid: #3f97d0;
    --ink: #111111;
    --muted: #9a9a9a;
    --panel: #f3f3f3;
    --white: #ffffff;
  }
  * { margin: 0; padding: 0; box-sizing: border-box; }
  html, body { width: 1130px; height: 1200px; overflow: hidden; }
  body { position: relative; background: var(--white); font-family: "Montserrat", sans-serif; color: var(--ink); }

  .site-header { position: absolute; left: 0; top: 0; width: 1130px; height: 70px; background: var(--brand-blue); }
  .brand { position: absolute; left: 152px; top: 22px; color: var(--white); font-family: "Montserrat", sans-serif; font-weight: 400; font-size: 22px; letter-spacing: 1px; line-height: 26px; }
  .main-nav { position: absolute; top: 29px; left: 0; width: 100%; }
  .main-nav a { position: absolute; color: var(--white); text-decoration: none; font-size: 9px; font-weight: 700; letter-spacing: 1.4px; line-height: 12px; }
  .lang svg { margin-left: 4px; vertical-align: 1px; }

  .section-title { position: absolute; left: 0; width: 1130px; text-align: center; font-weight: 700; font-size: 24px; letter-spacing: 6px; line-height: 30px; }
  .title-bar { position: absolute; left: 549px; width: 30px; height: 6px; background: var(--brand-blue); }

  .tile { position: absolute; width: 255px; height: 198px; display: flex; align-items: center; justify-content: center; }
  .tile span { color: var(--white); font-family: "Lato", sans-serif; font-weight: 900; font-size: 14px; letter-spacing: 0.3px; }
  .tile--light { background: linear-gradient(135deg, #62b8d2 0%, var(--tile-light) 55%, #4ea6c4 100%); box-shadow: 0 0 18px rgba(90,177,205,0.45); }
  .tile--dark { background: linear-gradient(135deg, #155a9e 0%, var(--tile-dark) 60%, #083f7c 100%); box-shadow: 0 0 18px rgba(40,40,80,0.35); }
  .tile--mid { background: linear-gradient(135deg, #4aa3d8 0%, var(--tile-mid) 60%, #2f86c2 100%); box-shadow: 0 0 18px rgba(40,40,80,0.3); }

  .more-button { position: absolute; left: 518px; top: 681px; width: 92px; height: 26px; background: var(--button-blue); border: 1px solid var(--brand-blue); color: var(--white); font-family: "Lato", sans-serif; font-weight: 900; font-size: 11px; display: flex; align-items: center; justify-content: center; letter-spacing: 0.3px; }

  .contact { position: absolute; left: 0; top: 779px; width: 1130px; height: 379px; background: var(--panel); }
  .address-label { position: absolute; left: 0; top: 940px; width: 1130px; text-align: center; color: var(--brand-blue); font-size: 9px; font-weight: 600; letter-spacing: 1px; }
  .address-rule { position: absolute; left: 536px; top: 961px; width: 56px; height: 1px; background: var(--brand-blue); }
  .address-line { position: absolute; left: 0; width: 1130px; text-align: center; color: var(--muted); font-size: 8.5px; font-weight: 500; letter-spacing: 1px; line-height: 10px; }
  .address-line b { color: #333333; font-weight: 600; }

  .site-footer { position: absolute; left: 0; top: 1158px; width: 1130px; height: 42px; background: var(--brand-blue); color: var(--white); font-size: 9px; font-weight: 700; letter-spacing: 1px; display: flex; align-items: center; justify-content: center; }
  .site-footer .sep { margin: 0 11px; }
</style>
</head>
<body>
  <header class="site-header">
    <div class="brand">Norvik Precision</div>
    <nav class="main-nav">
      <a style="left:598px">HOME</a>
      <a style="left:666px">LEISTUNGEN</a>
      <a style="left:765px">GALERIE</a>
      <a style="left:846px">UNTERNEHMEN</a>
      <a class="lang" style="left:953px">EN<svg width="7" height="4" viewBox="0 0 7 4"><path d="M0 0h7L3.5 4z" fill="#fff"/></svg></a>
    </nav>
  </header>

  <h2 class="section-title" style="top:127px">GALERIE</h2>
  <div class="title-bar" style="top:173px"></div>

  <div class="tile tile--light" style="left:152px;top:207px" role="img" aria-label="Photo of a machined gear part on technical drawings"><span>REVERSE ENGINEERING</span></div>
  <div class="tile tile--dark" style="left:437px;top:207px" role="img" aria-label="Photo of a CNC milling tool cutting a metal block"><span>PROTOTYPING</span></div>
  <div class="tile tile--light" style="left:722px;top:207px" role="img" aria-label="Photo of a cut metal part on technical drawings"><span>LASERSCAN</span></div>
  <div class="tile tile--light" style="left:152px;top:440px" role="img" aria-label="Photo of a machined gear part on technical drawings"><span>REVERSE ENGINEERING</span></div>
  <div class="tile tile--mid" style="left:437px;top:440px" role="img" aria-label="Photo of a CNC milling tool cutting a metal block"><span>PROTOTYPING</span></div>
  <div class="tile tile--light" style="left:722px;top:440px" role="img" aria-label="Photo of a cut metal part on technical drawings"><span>LASERSCAN</span></div>

  <div class="more-button">MORE</div>

  <section class="contact"></section>
  <h2 class="section-title" style="top:851px">KONTAKT</h2>
  <div class="title-bar" style="top:897px"></div>
  <div class="address-label">Address</div>
  <div class="address-rule"></div>
  <p class="address-line" style="top:984px">Ut enim ad minim veniam, quis nostrud</p>
  <p class="address-line" style="top:1002px">exercitation ullamco laboris</p>
  <p class="address-line" style="top:1012px">nisi ut aliquip ex ea commodo</p>
  <p class="address-line" style="top:1032px">consequat.Consectetur Lorem Ipsum</p>
  <p class="address-line" style="top:1053px">Tel : <b>+00 123456789</b></p>
  <p class="address-line" style="top:1073px">E-mail : <b>info@norvikprecision.com</b></p>

  <footer class="site-footer">
    <span>© 2018 Norvik Precision</span><span class="sep">/</span>
    <span>Impressum</span><span class="sep">/</span>
    <span>Datenschutzerklärung</span><span class="sep">/</span>
    <span>Haftungsausschluss</span>
  </footer>
</body>
</html>
```